New Digital Marketing Company Needs Web Design

Introduction

Brightcrest gives advice to small businesses about their websites and digital marketing strategies and builds working relationships with clients to understand their business and maximise its online presence.

Brightcrest offers services to support its clients needs such as: website auditing & search engine optimisation (SEO), Quorvo Promoline, Chatterlane advertising, newsletter development & management, online performance reporting, email setup & management, website hosting, maintenance & backup, web development, web updates & web design.

Design Specification

The site should have a clean & professional look and use the colour scheme from the logo (attached below).

The design should consist of 2 templates; The homepage & content page.

Homepage Design

The homepage should have a header with logo, contact number and email and menu. Followed underneath by a slider and then individual blocks for key services. Under the key services should be a testimonial block with 3 testimonials. Finally the footer with company details, menu links and location map.

Header Info:

Contact number: 01632 960481
Email: info@brightcrest-demo.co.uk

Menu: Home Services About Contact

Slider Design:

The slider should be full page and show an image with text.

Key Services:

The key services should have a relevant icon and brief description.

The key services are:

Digital Marketing

Website Hosting & Management

Website Health Check (SEO)

Website Updating & Development

Newsletter Management

Email Management

Note: Lorem Ipsum can be used for brief description...

Testimonials:

There should be 3 testimonials side by side and they should include a headshot image of the person giving the testimonial.

Note: Lorem Ipsum and sample images can be used for testimonials...

Footer:

The footer should have 3 sections:

Menu links:

Digital Marketing About
Quorvo Promoline Contact
Chatterlane Advertising Privacy Policy
Search Engine Optimisation (SEO) Terms & Conditions
Website Hosting FAQ
Newsletter Management

Company Information:

BrightCrest
14 Marlow Close
Bracknell
Berskhire
ZZ9 4QT
Tel: 01632 960481

Chatterlane icon - Pipwave icon - Careernest icon

Location

Quorvo map

Footer Bottom:

Copyright message.

Content Design

The content design should have the common header and footer.

Each content page should have a banner for image with text description (page title).

The content page should have area for text description and area for a video display if available.

There should be a right column (possibly) for modules (latest blog, latest Chatterlane feeds, testimonial)

Project Deadline Extended
Reason: I have had to extend the deadline as could not review while on vacation and need to feedback to some designers for content page design. Many thanks for your understanding.

Target Market(s)

Industry/Entity Type

Digital

Number of Pages Required

2 page

Requirements
Must have
• The site should have a clean & professional look and use the colour scheme from the logo (attached below).
• The design should consist of 2 templates; The homepage & content page.

```html
<!DOCTYPE html>
<html lang="en">
<head>
<meta charset="utf-8">
<title>Brightcrest – Digital Marketing</title>
<link rel="stylesheet" href="https://fonts.googleapis.com/css2?family=Open+Sans:wght@400;600;700&family=Oswald:wght@500;600&display=swap">
<style>
:root{
  --brand-purple:#3b2f5e;
  --brand-maroon:#6a1b3c;
  --ink:#333333;
  --ink-soft:#5f5f66;
  --ink-muted:#8a8a90;
  --rule:#e6e6ea;
  --white:#ffffff;
  --footer-bg:#ffffff;
  --map-tone:#e2e2e2;
  --band-dark:#4a4a4e;
}
*{box-sizing:border-box;margin:0;padding:0}
html,body{width:1200px;height:2281px;overflow:hidden}
body{font-family:"Open Sans",Arial,sans-serif;color:var(--ink);background:var(--white);position:relative}
.wrap{width:912px;margin:0 auto;position:relative}

/* header */
.site-header{height:94px;position:relative}
.brand{position:absolute;left:144px;top:22px;display:flex;align-items:center;gap:10px}
.brand-dot{width:34px;height:34px;border-radius:50%;background:var(--brand-purple)}
.brand-name{font-size:30px;font-weight:700;color:var(--brand-maroon);letter-spacing:-.5px}
.contact-block{position:absolute;top:0;height:94px;border-left:1px solid var(--rule);display:flex;align-items:center;gap:14px;padding-left:22px}
.contact-block.phone{left:627px;width:176px}
.contact-block.email{left:803px;width:272px;border-right:1px solid var(--rule)}
.contact-label{font-size:12px;color:var(--ink-soft);line-height:16px}
.contact-value{font-size:16px;font-weight:700;color:var(--brand-maroon);line-height:20px}
.contact-block svg{flex:none}

/* nav */
.main-nav{height:47px;border-top:1px solid var(--rule);border-bottom:1px solid var(--rule);position:relative}
.main-nav a{position:absolute;top:0;line-height:45px;font-size:13px;letter-spacing:1px;color:var(--ink);text-decoration:none}
.main-nav a.active{border-top:2px solid var(--brand-purple);line-height:41px;padding:0 20px;margin-left:-20px;color:var(--brand-purple)}

/* hero */
.hero{height:413px;position:relative;background:linear-gradient(100deg,#c9d6de 0%,#e6ecf0 30%,#f4f6f8 55%,#eef3f6 80%,#d8e6e4 100%)}
.hero-copy{position:absolute;right:144px;top:160px;text-align:right;width:560px}
.hero-title{font-family:"Oswald","Arial Narrow",sans-serif;font-weight:600;font-size:30px;letter-spacing:2.5px;color:var(--brand-purple)}
.hero-text{font-size:12px;line-height:19px;color:#5a5c8a;margin-top:8px}
.btn-outline{display:inline-block;margin-top:18px;width:156px;height:39px;line-height:37px;text-align:center;border:1px solid var(--brand-maroon);color:var(--brand-maroon);font-size:17px;font-weight:600;background:rgba(255,255,255,.6)}

/* services */
.services{height:641px;position:relative}
.section-title{text-align:center;font-size:24px;font-weight:700;letter-spacing:.5px;color:var(--ink)}
.section-rule{width:80px;height:2px;background:var(--brand-purple);margin:12px auto 0}
.services .section-title{padding-top:58px}
.service-list{position:absolute;left:144px;top:133px;width:477px;list-style:none}
.service-item{display:flex;gap:26px;height:120px;padding-top:20px;border-bottom:1px solid var(--rule)}
.service-item:last-child{border-bottom:0}
.service-icon{width:80px;height:80px;flex:none}
.service-name{font-size:13px;font-weight:600;color:var(--brand-purple);margin-top:10px}
.service-desc{font-size:11.5px;line-height:20px;color:var(--ink-soft);margin-top:10px}
.services-art{position:absolute;left:646px;top:206px;width:410px;height:366px;border-radius:8px;background:radial-gradient(circle at 50% 55%,#e96a5e 0,#d9564c 28%,#3f7db8 42%,#a8cde8 62%,#ffffff 80%)}

/* testimonials */
.testimonials{height:400px;position:relative;background:linear-gradient(120deg,#2f2f33 0%,#6b6b63 35%,#7c7a5e 55%,#4d5460 80%,#3c4250 100%)}
.testimonials .section-title{color:var(--white);padding-top:58px}
.testimonials .section-rule{background:var(--white)}
.quote-card{position:absolute;top:150px;width:288px;height:161px;background:rgba(255,255,255,.22)}
.quote-photo{position:absolute;left:16px;top:-19px;width:94px;height:94px;background:linear-gradient(160deg,#9aa3ad,#5d646e)}
.quote-name{position:absolute;left:126px;top:42px;font-size:15px;font-weight:700;color:var(--white)}
.quote-role{position:absolute;left:126px;top:64px;font-size:10px;color:#d8d8d8}
.quote-text{position:absolute;left:16px;top:95px;right:16px;font-size:12px;line-height:17px;color:var(--white)}
.slider-dots{position:absolute;top:332px;left:0;right:0;display:flex;justify-content:center;gap:12px}
.slider-dots span{width:6px;height:6px;border-radius:50%;background:rgba(255,255,255,.45)}
.slider-dots span.on{background:var(--white)}

/* footer */
.site-footer{height:274px;position:relative;background:var(--footer-bg)}
.footer-col{position:absolute;top:62px}
.footer-col h3{font-size:24px;font-weight:700;letter-spacing:.5px;color:var(--ink);margin-bottom:12px}
.footer-info{font-size:12px;line-height:19px;color:var(--ink);list-style:none}
.footer-info li{display:flex;gap:10px;margin-bottom:4px}
.footer-social{border-top:1px solid var(--rule);margin-top:10px;padding-top:12px;width:232px;display:flex;gap:18px}
.footer-social span{width:13px;height:13px;background:var(--brand-purple);opacity:.8}
.footer-links{list-style:none;font-size:12px;line-height:19.5px}
.footer-links li::before{content:"›";margin-right:8px;font-weight:700}
.newsletter-text{font-size:12px;line-height:19px;color:var(--ink);width:230px}
.newsletter-field{margin-top:16px;width:234px;border-bottom:1px solid var(--brand-maroon);display:flex;justify-content:space-between;align-items:center;padding-bottom:4px}
.newsletter-field span{font-size:10px;font-style:italic;color:var(--ink-muted)}

.location-map{height:359px;background:linear-gradient(135deg,#d6d6d6,#ececec 40%,#e0e0e0 70%,#efefef)}

.footer-bottom{height:51px;position:relative;font-size:11px}
.copyright{position:absolute;left:144px;top:17px;color:var(--ink-muted)}
.legal-links{position:absolute;right:144px;top:17px;display:flex;gap:24px}
.legal-links a{color:var(--ink);text-decoration:none}
</style>
</head>
<body>

<header class="site-header">
  <div class="brand"><span class="brand-dot"></span><span class="brand-name">BrightCrest</span></div>
  <div class="contact-block phone">
    <svg width="18" height="18" viewBox="0 0 24 24" aria-hidden="true"><path fill="#8a8a90" d="M6.6 10.8a15.1 15.1 0 0 0 6.6 6.6l2.2-2.2c.3-.3.7-.4 1-.2 1.1.4 2.3.6 3.6.6.6 0 1 .4 1 1V20c0 .6-.4 1-1 1A17 17 0 0 1 3 4c0-.6.4-1 1-1h3.5c.6 0 1 .4 1 1 0 1.3.2 2.5.6 3.6.1.3 0 .7-.2 1z"/></svg>
    <div><div class="contact-label">Contact us</div><div class="contact-value">01632 960481</div></div>
  </div>
  <div class="contact-block email">
    <svg width="22" height="16" viewBox="0 0 22 16" aria-hidden="true"><rect x="1" y="1" width="20" height="14" fill="none" stroke="#8a8a90" stroke-width="1.6"/><path d="M1 1l10 8 10-8" fill="none" stroke="#8a8a90" stroke-width="1.6"/></svg>
    <div><div class="contact-label">Email</div><div class="contact-value">info@brightcrest-demo.co.uk</div></div>
  </div>
</header>

<nav class="main-nav">
  <a class="active" href="#" style="left:164px">HOME</a>
  <a href="#" style="left:251px">SERVICES</a>
  <a href="#" style="left:362px">ABOUT</a>
  <a href="#" style="left:456px">CONTACT</a>
</nav>

<section class="hero" role="img" aria-label="Photo of hands typing on a white keyboard in a bright office">
  <div class="hero-copy">
    <h1 class="hero-title">DIGITAL MARKETING STRATEGY</h1>
    <p class="hero-text">We offers services to support its clients needs such as: website auditing &amp; search engine optimisation (SEO),Quorvo Promoline, Chatterlane advertising,...</p>
    <a class="btn-outline">Get started</a>
  </div>
</section>

<section class="services">
  <h2 class="section-title">OUR SERVICES</h2>
  <div class="section-rule"></div>
  <ul class="service-list">
    <li class="service-item">
      <svg class="service-icon" viewBox="0 0 80 80" aria-hidden="true"><circle cx="40" cy="40" r="38" fill="none" stroke="#3b2f5e" stroke-width="2"/><circle cx="35" cy="34" r="14" fill="none" stroke="#3b2f5e" stroke-width="3"/><path d="M45 44l14 14" stroke="#3b2f5e" stroke-width="6" stroke-linecap="round"/><text x="35" y="38" font-size="9" font-family="Open Sans,sans-serif" font-weight="700" text-anchor="middle" fill="#3b2f5e">SEO</text></svg>
      <div><h3 class="service-name">Website Health Check (SEO)</h3><p class="service-desc">Proven search engine optimization services to gain visibility, awareness and leads for your company...</p></div>
    </li>
    <li class="service-item">
      <svg class="service-icon" viewBox="0 0 80 80" aria-hidden="true"><circle cx="40" cy="40" r="38" fill="none" stroke="#3b2f5e" stroke-width="2"/><path d="M24 56l30-30" stroke="#3b2f5e" stroke-width="5" stroke-linecap="round"/><path d="M26 24l30 32" stroke="#3b2f5e" stroke-width="5" stroke-linecap="round"/><circle cx="56" cy="24" r="7" fill="none" stroke="#3b2f5e" stroke-width="3"/></svg>
      <div><h3 class="service-name">Website Updating &amp; Development</h3><p class="service-desc">Website maintenance is vital to effectively communicating your brand and providing the best possible user ...</p></div>
    </li>
    <li class="service-item">
      <svg class="service-icon" viewBox="0 0 80 80" aria-hidden="true"><circle cx="40" cy="40" r="38" fill="none" stroke="#3b2f5e" stroke-width="2"/><rect x="20" y="27" width="40" height="27" fill="#3b2f5e"/><path d="M20 27l20 16 20-16" fill="none" stroke="#fff" stroke-width="2"/></svg>
      <div><h3 class="service-name">Newsletter &amp; Email Management</h3><p class="service-desc">Newsletters are a great tool to create customer loyalty, to identify you as an expert in your field, and to create...</p></div>
    </li>
    <li class="service-item">
      <svg class="service-icon" viewBox="0 0 80 80" aria-hidden="true"><circle cx="40" cy="40" r="38" fill="none" stroke="#3b2f5e" stroke-width="2"/><path d="M30 22l0 36 9-9 7 14 5-3-7-13 12 0z" fill="#3b2f5e"/></svg>
      <div><h3 class="service-name">Digital Marketing</h3><p class="service-desc">Companies trust us to manage their online presence, monitor the internet for online mentions ...</p></div>
    </li>
  </ul>
  <div class="services-art" role="img" aria-label="Illustration of a laptop surrounded by gears, a cloud, a clock and rising arrows"></div>
</section>

<section class="testimonials" role="group" aria-label="Testimonials over a photo of a hand touching a digital interface">
  <h2 class="section-title">TESTIMONIALS</h2>
  <div class="section-rule"></div>
  <article class="quote-card" style="left:144px">
    <div class="quote-photo" role="img" aria-label="Headshot of Mr. John Doe"></div>
    <div class="quote-name">Mr.John Doe</div>
    <div class="quote-role">Ceo at Velmora</div>
    <p class="quote-text">"Lorem Ipsum is simply dummy text of the printing and typesetting industry."</p>
  </article>
  <article class="quote-card" style="left:455px">
    <div class="quote-photo" role="img" aria-label="Headshot of Ms. Hana"></div>
    <div class="quote-name">Ms.Hana</div>
    <div class="quote-role">Designer at Tandlow</div>
    <p class="quote-text">"Lorem Ipsum is simply dummy text of the printing and typesetting industry."</p>
  </article>
  <article class="quote-card" style="left:768px">
    <div class="quote-photo" role="img" aria-label="Headshot of Mr. Tony"></div>
    <div class="quote-name">Mr.Tony</div>
    <div class="quote-role">Designer at Orbisk</div>
    <p class="quote-text">"Lorem Ipsum is simply dummy text of the printing and typesetting industry."</p>
  </article>
  <div class="slider-dots"><span class="on"></span><span></span><span></span></div>
</section>

<footer class="site-footer">
  <div class="footer-col" style="left:144px">
    <h3>BRIGHTCREST</h3>
    <ul class="footer-info">
      <li><svg width="10" height="14" viewBox="0 0 10 14" aria-hidden="true"><path d="M5 0a5 5 0 0 1 5 5c0 4-5 9-5 9S0 9 0 5a5 5 0 0 1 5-5z" fill="#333"/><circle cx="5" cy="5" r="1.8" fill="#fff"/></svg><span>14 Marlow Close - Bracknell - Berskhire<br>- ZZ9 4QT</span></li>
      <li><svg width="11" height="11" viewBox="0 0 24 24" aria-hidden="true"><path fill="#333" d="M6.6 10.8a15.1 15.1 0 0 0 6.6 6.6l2.2-2.2c.3-.3.7-.4 1-.2 1.1.4 2.3.6 3.6.6.6 0 1 .4 1 1V20c0 .6-.4 1-1 1A17 17 0 0 1 3 4c0-.6.4-1 1-1h3.5c.6 0 1 .4 1 1 0 1.3.2 2.5.6 3.6.1.3 0 .7-.2 1z"/></svg><span>Tel: 01632 960481</span></li>
    </ul>
    <div class="footer-social">
      <span aria-label="Chatterlane"></span><span aria-label="Pipwave"></span><span aria-label="Careernest"></span>
    </div>
  </div>
  <div class="footer-col" style="left:456px">
    <h3>OUR SERVICE</h3>
    <ul class="footer-links">
      <li>Digital Marketing</li>
      <li>Quorvo Promoline</li>
      <li>Chatterlane Advertising</li>
      <li>Search Engine Optimisation (SEO)</li>
      <li>Website Hosting</li>
      <li>Newsletter Management</li>
    </ul>
  </div>
  <div class="footer-col" style="left:767px">
    <h3>NEWSLETTER</h3>
    <p class="newsletter-text">Don't miss to subscribe to our news feeds, kindly fill the form below.</p>
    <div class="newsletter-field"><span>You email Address</span>
      <svg width="10" height="10" viewBox="0 0 10 10" aria-hidden="true"><path d="M0 5h8M5 1l4 4-4 4" fill="none" stroke="#6a1b3c" stroke-width="2"/></svg></div>
  </div>
</footer>

<div class="location-map" role="img" aria-label="Greyscale street map showing the office location"></div>

<div class="footer-bottom">
  <p class="copyright">Copyright © 2016 Brightcrest.</p>
  <nav class="legal-links"><a href="#">About</a><a href="#">Contact</a><a href="#">Privacy Policy</a><a href="#">Terms &amp; Conditions</a><a href="#">FAQ</a></nav>
</div>

</body>
</html>
```